Los Robles Ember Chicken MENU!

We are looking for a simple, rustic and modern menu that highlights our passion for healthy and tasty chickens!
We want to highlight our menu but yet keep it very simple.

Attached is info on our logo and our menu information

Target Market(s)

We want to attract all customers but primarily we want to focus on the following 3 markets: Healthy concerned, Food fanatics and Family based.

Industry/Entity Type

Fast Food Restaurant

Requirements
Must have
• We must have our logo on the flyer,
• rustic yet modern
• you must use our colors on the flyer and
• KEEP IT SIMPLE
• Here is our Menu below
• Attached is our final menu we are going to advertise:
• Chicken:
• 1/4 Chicken Dark $6.99
• 1/4 Chicken White $7.99
• 1/2 Chicken white + dark $9.99
• 1/2 chicken all white $10.99
• All come with choice of 2 small sides
• 1 whole chicken family meal ( served with 3 Large sides + 2 liter soda) $23.99
• 2 whole chicken family meal (served with 4 Large sides + 2 liter soda) $33.99
• Extra whole chicken (Chicken only) $13.99
• Sides available with meals:
• - Cilantro infused white rice
• - Hand Cut Fries
• - Hand Cut Sweet potato Fries
• - Yucca
• - Fried Plantains
• - Pinto Beans
• - Black Beans
• - Steamed vegetable medley
• - Cesar Salad
• - Garden Salad
• - House Salad
• - Tortillas
• (reg side: $1.99) Large Side $3.29
• Other Dishes available:
• Lomo Saltado: $12.99
• Pesto Pasta (Tallarin Verde) w/ Steak or 1/4 chicken $ 12.99
• Bistek a lo Pobre: $12.99
• Marcos Favorite $12.99 (Chicken filet grilled) w/ salads
• Tallarin Saltado (Garden style pasta) w/ Chicken $11.99, Steak add. $1.49
• Tallarin a la Huancaina $12.99 w/ steak or 1/4 chicken
• Garden Salad ($6.99) Add chicken or steak $1.99
• Cesar Salad ($6.99) Add Chicken or steak $1.99
• House Salad ($6.99) Add chicken or steak $1.99
• DRINKS/DESSERTS:
• - SODAS: REG. $1.99 LARGE 2.59
• - SOLA FIZZ: $1.69 CAN; $1.99 IMPORTED; $2.59 BOTTLE
• - SPECIALTY DRINKS: $2.59
• - ALFAJOR $2.99
• - PERUVIAN FLAN $4.99
• - 3 LECHES $4.99
• (SAVE $1.00 OF ANY DESSERT WITH PURCHASE OF MEAL)
Nice to have
• We would love to see it all in 1 half sheet
Should not have
• can not have too much on it where its confusing.

```html
<!DOCTYPE html>
<html lang="en">
<head>
<meta charset="utf-8">
<title>Los Robles Ember Chicken Menu</title>
<link href="https://fonts.googleapis.com/css2?family=Roboto+Condensed:ital,wght@0,400;0,700;1,400;1,700&display=swap" rel="stylesheet">
<style>
  :root {
    --orange: #f07322;
    --green: #8cc63f;
    --dark: #1f1f1f;
    --dark-2: #2c2c2c;
    --white: #ffffff;
    --line: #d9d9d9;
    --leader: #8a8a8a;
    --canvas: #e6e6e6;
  }
  * { box-sizing: border-box; margin: 0; padding: 0; }
  html, body { width: 1200px; height: 1200px; overflow: hidden; }
  body {
    background: var(--canvas);
    font-family: "Roboto Condensed", Arial, sans-serif;
    color: var(--white);
    position: relative;
  }
  .sheet {
    position: absolute;
    top: 205px;
    width: 560px;
    height: 790px;
    overflow: hidden;
    background: linear-gradient(90deg, var(--dark) 0%, var(--dark-2) 50%, var(--dark) 100%);
    box-shadow: 0 6px 18px rgba(0,0,0,.25);
  }
  .sheet--front { left: 30px; }
  .sheet--back { left: 610px; }
  .wave { position: absolute; left: 0; width: 100%; display: block; }
  .photo {
    position: absolute;
    border-radius: 50%;
    background: radial-gradient(circle at 45% 40%, #d08a3c 0%, #a95a22 45%, #eeeeee 70%, #dcdcdc 100%);
  }
  .photo--salad {
    background: radial-gradient(circle at 50% 50%, #7fb84a 0%, #d9413a 40%, #eeeeee 68%, #dcdcdc 100%);
  }
  .photo--stew {
    background: radial-gradient(circle at 50% 50%, #e3742a 0%, #c4541c 40%, #1a1a1a 70%, #111 100%);
  }
  .brand {
    position: absolute;
    top: 48px;
    right: 30px;
    display: flex;
    align-items: center;
    gap: 8px;
    color: var(--orange);
    font-weight: 700;
    font-size: 17px;
  }
  .brand__dot { width: 18px; height: 18px; border-radius: 50%; background: var(--orange); }
  .panel {
    position: absolute;
    border: 1.5px solid var(--line);
    border-radius: 12px;
    padding: 28px 20px 14px;
  }
  .panel__tab {
    position: absolute;
    top: -11px;
    left: 50%;
    transform: translateX(-50%);
    background: var(--orange);
    color: var(--white);
    font-weight: 700;
    font-size: 14px;
    letter-spacing: .5px;
    padding: 2px 14px;
    border-radius: 3px;
    white-space: nowrap;
  }
  .sheet--front .panel { font-style: italic; }
  .row { display: flex; align-items: baseline; font-size: 12.5px; line-height: 17px; text-transform: uppercase; }
  .row__leader { flex: 1; border-bottom: 1px dotted var(--leader); margin: 0 5px; transform: translateY(-3px); }
  .row__price { color: var(--orange); font-weight: 700; }
  .row--strong { font-weight: 700; margin-top: 6px; }
  .note { font-size: 10.5px; line-height: 13px; color: #dcdcdc; text-transform: none; }
  .callout { color: var(--green); font-weight: 700; font-size: 14px; margin: 8px 0 4px 20px; letter-spacing: .3px; }
  .sides { display: flex; justify-content: space-between; font-size: 14px; line-height: 19px; }
  .sides ul { list-style: none; }
  .side-price { position: absolute; color: var(--orange); font-weight: 700; font-size: 17px; }
  .site {
    position: absolute;
    bottom: 26px;
    left: 26px;
    display: flex;
    align-items: center;
    gap: 7px;
    color: #1f1f1f;
    font-size: 14px;
  }
  .site svg { width: 18px; height: 18px; }
  .sheet--back .row { font-size: 11.5px; line-height: 15px; }
  .sheet--back .note { font-size: 9.5px; line-height: 11px; }
  .group-head { font-weight: 700; font-size: 12px; line-height: 15px; margin-top: 4px; }
</style>
</head>
<body>

<!-- Front sheet -->
<section class="sheet sheet--front">
  <svg class="wave" style="top:0" height="150" viewBox="0 0 560 150" preserveAspectRatio="none" aria-hidden="true">
    <path d="M0 0H560V118C470 150 360 150 260 110C170 76 80 70 0 80Z" fill="var(--orange)"/>
    <path d="M0 0H560V112C470 142 360 140 260 102C170 70 80 60 0 68Z" fill="var(--green)"/>
    <path d="M0 0H560V104C470 134 360 132 260 94C170 62 80 52 0 58Z" fill="var(--white)"/>
  </svg>
  <div class="photo" style="left:40px;top:8px;width:210px;height:92px" role="img" aria-label="Roast chicken with potato wedges on a white plate"></div>
  <div class="brand"><span class="brand__dot"></span>Los Robles Ember Chicken</div>

  <div class="panel" style="top:150px;left:30px;right:30px;height:260px">
    <span class="panel__tab">CHICKEN</span>
    <div class="row"><span>1/4 Chicken Dark</span><span class="row__leader"></span><span class="row__price">$06.99</span></div>
    <div class="row"><span>1/4 Chicken White</span><span class="row__leader"></span><span class="row__price">$07.99</span></div>
    <div class="row"><span>1/2 Chicken White + Dark</span><span class="row__leader"></span><span class="row__price">$09.99</span></div>
    <div class="row"><span>1/2 Chicken All White</span><span class="row__leader"></span><span class="row__price">$10.99</span></div>
    <p class="callout">ALL COME WITH CHOICE OF 2 SMALL SIDES</p>
    <div class="row row--strong"><span>1 Whole Chicken Family Meal</span><span class="row__leader"></span><span class="row__price">$23.99</span></div>
    <p class="note">(served with 3 Large sides + 2 liter soda)</p>
    <div class="row row--strong"><span>2 Whole Chicken Family Meal</span><span class="row__leader"></span><span class="row__price">$33.99</span></div>
    <p class="note">(served with 4 Large sides + 2 liter soda)</p>
    <div class="row row--strong"><span>Extra Whole Chicken <span class="note">(Chicken only)</span></span><span class="row__leader"></span><span class="row__price">$13.99</span></div>
  </div>

  <div class="panel" style="top:432px;left:30px;right:30px;height:232px">
    <span class="panel__tab">SIDES AVAILABLE WITH MEALS</span>
    <div class="sides">
      <ul>
        <li>Cilantro infused white rice</li>
        <li>Hand Cut Fries</li>
        <li>Hand Cut Sweet potato Fries</li>
        <li>Yucca</li>
        <li>Fried Plantains</li>
        <li>Pinto Beans</li>
      </ul>
      <ul>
        <li>Black Beans</li>
        <li>Steamed vegetable medley</li>
        <li>Cesar Salad</li>
        <li>Garden Salad</li>
        <li>House Salad</li>
        <li>Tortillas</li>
      </ul>
    </div>
    <div class="photo photo--stew" style="left:200px;top:40px;width:80px;height:50px" role="img" aria-label="Bowl of sauced chicken with rice"></div>
    <div class="photo photo--salad" style="left:150px;top:140px;width:120px;height:52px" role="img" aria-label="Plate of fresh garden salad"></div>
    <span class="side-price" style="left:20px;top:170px">REG SIDE: $1.99</span>
    <span class="side-price" style="right:22px;top:196px">LARGE SIDE $3.29</span>
  </div>

  <svg class="wave" style="bottom:0" height="120" viewBox="0 0 560 120" preserveAspectRatio="none" aria-hidden="true">
    <path d="M0 40C120 10 260 20 380 60C450 84 510 80 560 60V120H0Z" fill="var(--white)"/>
    <path d="M0 56C120 26 260 36 380 76C450 100 510 96 560 76V120H0Z" fill="var(--orange)"/>
    <path d="M0 64C120 36 260 46 380 86C450 110 510 106 560 88V120H0Z" fill="var(--green)"/>
  </svg>
  <div class="site">
    <svg viewBox="0 0 20 20" aria-hidden="true"><circle cx="10" cy="10" r="8.5" fill="none" stroke="#1f1f1f" stroke-width="1.6"/><ellipse cx="10" cy="10" rx="3.8" ry="8.5" fill="none" stroke="#1f1f1f" stroke-width="1.4"/><path d="M1.5 10H18.5M3 5.5H17M3 14.5H17" stroke="#1f1f1f" stroke-width="1.3"/></svg>
    www.losroblesember.com
  </div>
  <div class="photo" style="right:50px;bottom:18px;width:150px;height:70px" role="img" aria-label="Roast chicken with vegetables on a white plate"></div>
</section>

<!-- Back sheet -->
<section class="sheet sheet--back">
  <svg class="wave" style="top:0;height:100%" viewBox="0 0 560 790" preserveAspectRatio="none" aria-hidden="true">
    <path d="M0 0H150C70 60 40 200 36 400C32 560 20 650 0 700Z" fill="var(--orange)"/>
    <path d="M150 0H160C84 60 52 200 48 400C44 560 30 660 0 720V700C20 650 32 560 36 400C40 200 70 60 150 0Z" fill="var(--white)"/>
  </svg>

  <div class="panel" style="top:40px;left:100px;right:26px;height:412px">
    <span class="panel__tab" style="font-size:12px">OTHER DISHES AVAILABLE</span>
    <div class="row"><span>Lomo Saltado</span><span class="row__leader"></span><span class="row__price">$12.99</span></div>
    <div class="row"><span>Pesto Pasta (Tallarin Verde)</span><span class="row__leader"></span><span class="row__price">$12.99</span></div>
    <p class="note">w/ Steak or 1/4 chicken</p>
    <div class="row"><span>Bistek a lo Pobre</span><span class="row__leader"></span><span class="row__price">$12.99</span></div>
    <div class="row"><span>Marcos Favorite</span><span class="row__leader"></span><span class="row__price">$12.99</span></div>
    <p class="note">(Chicken filet grilled) w/ salads</p>
    <div class="row"><span>Tallarin Saltado</span><span class="row__leader"></span><span class="row__price">$11.99</span></div>
    <p class="note">(Garden style pasta) w/ Chicken</p>
    <div class="row"><span>Steak add.</span><span class="row__leader"></span><span class="row__price">$01.49</span></div>
    <div class="row"><span>Tallarin a la Huancaina</span><span class="row__leader"></span><span class="row__price">$12.99</span></div>
    <p class="note">w/ steak or 1/4 chicken</p>
    <div class="row"><span>Garden Salad</span><span class="row__leader"></span><span class="row__price">$06.99</span></div>
    <div class="row"><span>Add chicken or steak</span><span class="row__leader"></span><span class="row__price">$01.99</span></div>
    <div class="row"><span>Cesar Salad</span><span class="row__leader"></span><span class="row__price">$06.99</span></div>
    <div class="row"><span>Add chicken or steak</span><span class="row__leader"></span><span class="row__price">$01.99</span></div>
    <div class="row"><span>House Salad</span><span class="row__leader"></span><span class="row__price">$06.99</span></div>
    <div class="row"><span>Add chicken or steak</span><span class="row__leader"></span><span class="row__price">$01.99</span></div>
  </div>

  <div class="panel" style="top:474px;left:100px;right:26px;height:210px;padding-top:22px">
    <span class="panel__tab">DRINKS/DESSERTS</span>
    <p class="group-head">SODAS:</p>
    <div class="row"><span>Reg</span><span class="row__leader"></span><span class="row__price">$01.99</span></div>
    <div class="row"><span>Large</span><span class="row__leader"></span><span class="row__price">$02.59</span></div>
    <p class="group-head">SOLA FIZZ:</p>
    <div class="row"><span>Can</span><span class="row__leader"></span><span class="row__price">$01.69</span></div>
    <div class="row"><span>Imported</span><span class="row__leader"></span><span class="row__price">$01.99</span></div>
    <div class="row"><span>Bottle</span><span class="row__leader"></span><span class="row__price">$02.59</span></div>
    <div class="row"><span>Specialty Drinks</span><span class="row__leader"></span><span class="row__price">$02.59</span></div>
    <div class="row"><span>Alfajor</span><span class="row__leader"></span><span class="row__price">$02.99</span></div>
    <div class="row"><span>Peruvian Flan</span><span class="row__leader"></span><span class="row__price">$04.99</span></div>
    <div class="row"><span>3 Leches</span><span class="row__leader"></span><span class="row__price">$04.99</span></div>
  </div>

  <svg class="wave" style="bottom:0" height="110" viewBox="0 0 560 110" preserveAspectRatio="none" aria-hidden="true">
    <path d="M0 20C150 0 300 10 420 40C480 55 530 60 560 56V110H0Z" fill="var(--orange)"/>
    <path d="M0 32C150 12 300 22 420 52C480 67 530 72 560 68V110H0Z" fill="var(--white)"/>
    <path d="M0 46C150 26 300 36 420 66C480 81 530 86 560 82V110H0Z" fill="var(--green)"/>
  </svg>
</section>

</body>
</html>
```